Serial Entrepreneur Business Card: 4 Logo Design

I am a serial entrepreneur and a full time mechanical engineer. I have four businesses. I would like to display them all on one business card.
*Please see the attached PDF for the design requirements*

www.KelbroNest.com

Businesses
-KelbroNest
-Quiet Lantern Properties
-Torlen Products
-Drosk Harbor Cast

Target Market(s)

Clients, Entrepreneurs, Associates, really anyone. Should be very professional.

Industry/Entity Type

Entrepreneur

Contact Information for Business Card

3.5" x 2" Standard Business Card Size
** Please review the attached requirement PDF for in depth detail on what I am expecting**

Font styles to use
Sans Serif

Requirements
Must have
• My personal contact information:
• First Name: Dae hwan
• Last Name: Pellow
• Nick Name: Riko
• Address: 83 Tolmer Court, Garfield NJ 07392
• Phone Number: 201-574-2916
• Email: RikodPellow@mailnest.example
• Website: www.KelbroNest.com
• All Four Logos of the Companies I own:
• -KelbroNest
• -Quiet Lantern Properties
• -Torlen Products
• -Drosk Harbor Cast
• My Professions:
• -Prototyping Engineer
• -Real Estate Investor
• -Financial Blogger
• -Video Podcaster
• -Online Retail Seller
Nice to have
• If it fits, please include the website for each logo, if there is more space please include the email for each.
• It might be nice to have the QX GUILD Logo, or TOVRA logo for my full-time job. But only if it fits.

```html
<!DOCTYPE html>
<html lang="en">
<head>
<meta charset="utf-8">
<title>Dae hwan "Riko" Pellow – Business Card</title>
<link rel="stylesheet" href="https://fonts.googleapis.com/css2?family=Arimo:ital,wght@0,400;0,700;1,400&display=swap">
<style>
  :root{
    --bg:#ecebe7;
    --card:#ffffff;
    --green:#1e8a1e;
    --yellow:#d6c62c;
    --ink:#222222;
    --muted:#444444;
  }
  *{box-sizing:border-box;margin:0;padding:0}
  html,body{width:1200px;height:1060px;overflow:hidden}
  body{background:var(--bg);font-family:"Arimo",Arial,sans-serif;color:var(--ink);position:relative}
  .card{position:absolute;top:150px;width:440px;height:760px;background:var(--card);
        box-shadow:0 4px 14px rgba(0,0,0,.18);text-align:center}
  .card--front{left:140px}
  .card--back{left:620px}

  /* front */
  .owner-name{color:var(--green);font-weight:700;font-size:23px;margin-top:110px}
  .professions{list-style:none;display:inline-block;text-align:left;margin-top:26px}
  .professions li{font-style:italic;font-size:17px;color:var(--muted);line-height:23px}
  .professions .bullet{font-style:normal;font-weight:700;font-size:12px;margin-right:8px;display:inline-block;width:8px}
  .professions li:nth-child(odd) .bullet{color:var(--yellow)}
  .professions li:nth-child(even) .bullet{color:var(--green)}
  .rule{height:3px;background:var(--yellow);margin:0 auto}
  .card--front .rule{width:310px;margin-top:16px}
  .contacts{list-style:none;margin-top:12px}
  .contacts li{font-size:17px;line-height:22px;margin-bottom:8px}
  .contact-icon{display:block;width:24px;height:24px;margin:0 auto 3px}
  .brand-row{position:absolute;left:0;right:0;bottom:70px;display:flex;justify-content:space-around;align-items:center;padding:0 18px}
  .brand-chip{display:flex;align-items:center;gap:5px;font-size:12px;font-weight:700;color:var(--ink)}
  .brand-chip i{width:9px;height:9px;background:var(--green);display:block}

  /* back */
  .venture{padding-top:28px}
  .venture + .venture{padding-top:20px}
  .venture-mark{font-weight:700;font-size:26px;color:var(--ink);height:40px;line-height:40px}
  .venture-role{color:var(--green);font-weight:700;font-size:17px;margin-top:8px}
  .venture-email{font-size:16px;margin-top:6px}
  .venture-web{font-size:15px;color:var(--muted);margin-top:4px}
  .card--back .rule{width:310px;margin-top:14px}
</style>
</head>
<body>

<section class="card card--front">
  <h1 class="owner-name">Dae hwan «Riko» Pellow</h1>
  <ul class="professions">
    <li><span class="bullet">$</span>Prototyping Engineer</li>
    <li><span class="bullet">$</span>Real Estate Investor</li>
    <li><span class="bullet">$</span>Financial Blogger</li>
    <li><span class="bullet">$</span>Video Podcaster</li>
    <li><span class="bullet">$</span>Online Retail Seller</li>
  </ul>
  <div class="rule"></div>
  <ul class="contacts">
    <li>
      <svg class="contact-icon" viewBox="0 0 24 24"><circle cx="12" cy="12" r="11" fill="#fff" stroke="#d6c62c" stroke-width="2"/><rect x="8.5" y="5.5" width="7" height="13" rx="1.2" fill="none" stroke="#1e8a1e" stroke-width="1.6"/></svg>
      201-574-2916
    </li>
    <li>
      <svg class="contact-icon" viewBox="0 0 24 24"><circle cx="12" cy="12" r="11" fill="#fff" stroke="#d6c62c" stroke-width="2"/><rect x="6" y="8" width="12" height="8" fill="#1e8a1e"/><path d="M6 8l6 5 6-5" fill="none" stroke="#fff" stroke-width="1.3"/></svg>
      RikodPellow@mailnest.example
    </li>
    <li>
      <svg class="contact-icon" viewBox="0 0 24 24"><circle cx="12" cy="12" r="11" fill="#fff" stroke="#d6c62c" stroke-width="2"/><g fill="none" stroke="#1e8a1e" stroke-width="1.4"><circle cx="12" cy="12" r="6"/><ellipse cx="12" cy="12" rx="2.6" ry="6"/><path d="M6 12h12M7 9h10M7 15h10"/></g></svg>
      www.KelbroNest.com
    </li>
    <li>
      <svg class="contact-icon" viewBox="0 0 24 24"><circle cx="12" cy="12" r="11" fill="#fff" stroke="#d6c62c" stroke-width="2"/><path d="M12 19s-5-5.5-5-9a5 5 0 0 1 10 0c0 3.5-5 9-5 9z" fill="#1e8a1e"/><circle cx="12" cy="10" r="1.8" fill="#fff"/></svg>
      83 Tolmer Court, Orlow Falls QV 07392
    </li>
  </ul>
  <div class="rule"></div>
  <div class="brand-row">
    <span class="brand-chip"><i></i>KelbroNest</span>
    <span class="brand-chip"><i></i>Drosk Harbor Cast</span>
    <span class="brand-chip"><i></i>Quiet Lantern</span>
    <span class="brand-chip"><i></i>Torlen</span>
  </div>
</section>

<section class="card card--back">
  <article class="venture">
    <div class="venture-mark">KelbroNest</div>
    <div class="venture-role">Financial Blogger</div>
    <div class="venture-email">Riko@KelbroNest.com</div>
    <div class="venture-web">www.KelbroNest.com</div>
    <div class="rule"></div>
  </article>
  <article class="venture">
    <div class="venture-mark">Torlen Products</div>
    <div class="venture-role">Online Retail Seller</div>
    <div class="venture-email">Sales@TorlenProducts.com</div>
    <div class="venture-web">www.TorlenProducts.com</div>
    <div class="rule"></div>
  </article>
  <article class="venture">
    <div class="venture-mark">Drosk Harbor Cast</div>
    <div class="venture-role">Vlogger</div>
    <div class="venture-email">Media@DroskHarborCast.com</div>
    <div class="venture-web">www.DroskHarborCast.com</div>
    <div class="rule"></div>
  </article>
  <article class="venture">
    <div class="venture-mark">Quiet Lantern Properties</div>
    <div class="venture-role">Real Estate Investing</div>
    <div class="venture-email">Riko@QuietLanternProperties.com</div>
    <div class="venture-web">www.QuietLanternProperties.com</div>
  </article>
</section>

</body>
</html>
```